CRPG is needing business cards, and stationary created.

Pixel Forge created a logo for our business, and now we are wanting business cards, and stationary. I have included two designs of the same logo. Please feel free to use them as you want. The name of the company is Cedar Ridge Property Group LLC, the address is 812 NE Willow Ln., Suite 9, the city & state is Alder Grove, Montana, zip code is 97815, Telephone number is 555-327-4489, Fax number is 555-327-6051, the name on the business card is Carl Whitby CMCA

Industry/Entity Type

Property Management

Contact Information for Business Card

The card needs to look professional. Upscale.

Requirements
Must have
• The colors we are using are on the logo that has been uploaded.

```html
<!DOCTYPE html>
<html lang="en">
<head>
<meta charset="utf-8">
<title>Cedar Ridge Property Group — Letterhead</title>
<link href="https://fonts.googleapis.com/css2?family=Libre+Baskerville:wght@400;700&display=swap" rel="stylesheet">
<style>
  :root {
    --paper: #ffffff;
    --brand-green: #2dba5f;
    --brand-navy: #263d5e;
    --crop-mark: #444444;
    --watermark: #d6dce3;
  }
  html, body {
    margin: 0;
    padding: 0;
    width: 1200px;
    height: 1000px;
    overflow: hidden;
    background: var(--paper);
  }
  .letterhead {
    position: relative;
    width: 1200px;
    height: 1000px;
    background: var(--paper);
    font-family: "Libre Baskerville", "Times New Roman", serif;
  }
  .crop-marks {
    position: absolute;
    inset: 0;
  }
  .brand {
    position: absolute;
    left: 259px;
    top: 56px;
    display: flex;
    align-items: center;
    gap: 14px;
  }
  .brand-square {
    width: 52px;
    height: 52px;
    background: var(--brand-navy);
  }
  .brand-name {
    font-weight: 700;
    font-size: 26px;
    letter-spacing: 0.5px;
    color: var(--brand-green);
    line-height: 1;
  }
  .sender {
    position: absolute;
    left: 259px;
    top: 141px;
    margin: 0;
    font-style: normal;
  }
  .sender-name {
    font-weight: 700;
    font-size: 13px;
    color: var(--brand-green);
    margin: 0 0 1px;
    letter-spacing: 0.2px;
  }
  .sender-line {
    display: block;
    font-size: 10.5px;
    line-height: 14px;
    color: var(--brand-navy);
  }
  .watermark {
    position: absolute;
    left: 636px;
    top: 725px;
    width: 296px;
    font-weight: 700;
    font-size: 88px;
    line-height: 1;
    color: var(--watermark);
    text-align: center;
    letter-spacing: 0;
  }
</style>
</head>
<body>
<div class="letterhead">
  <svg class="crop-marks" width="1200" height="1000" viewBox="0 0 1200 1000" aria-hidden="true">
    <g stroke="var(--crop-mark)" stroke-width="0.75">
      <line x1="243" y1="0" x2="243" y2="32"/>
      <line x1="955" y1="0" x2="955" y2="32"/>
      <line x1="204" y1="38.5" x2="236" y2="38.5"/>
      <line x1="962" y1="38.5" x2="994" y2="38.5"/>
      <line x1="204" y1="961.5" x2="236" y2="961.5"/>
      <line x1="962" y1="961.5" x2="994" y2="961.5"/>
      <line x1="243" y1="968" x2="243" y2="1000"/>
      <line x1="955" y1="968" x2="955" y2="1000"/>
    </g>
  </svg>

  <div class="brand">
    <span class="brand-square" aria-hidden="true"></span>
    <span class="brand-name">CEDAR RIDGE</span>
  </div>

  <address class="sender">
    <p class="sender-name">CARL WHITBY, CMCA</p>
    <span class="sender-line">812 NE WILLOW LN.</span>
    <span class="sender-line">SUITE 9</span>
    <span class="sender-line">ALDER GROVE, MONTANA</span>
    <span class="sender-line">97815</span>
    <span class="sender-line">P: 555.327.4489</span>
    <span class="sender-line">F: 555.327.6051</span>
  </address>

  <div class="watermark" aria-hidden="true">CRPG</div>
</div>
</body>
</html>
```